Website design for lighting products company

We want a design for our website. The website is for a company that sells lighting products. The structure is similar to the below website. We really like their design as well: www.brambleshorelamps.com

Industry/Entity Type

Lighting

Number of Pages Required

5+ page

Colors

Designer to choose colors to be used in the design.

Requirements
Must have
• Simple design

```html
<!DOCTYPE html>
<html lang="en">
<head>
<meta charset="utf-8">
<title>Orrin Lighting</title>
<link rel="stylesheet" href="https://fonts.googleapis.com/css2?family=Jost:wght@400;500;600&family=Poppins:wght@400;500&display=swap">
<style>
:root{
  --navy:#0b1656;
  --navy-deep:#081040;
  --blue:#2444b8;
  --ink:#222;
  --muted:#555;
  --grey-bg:#f0f0f0;
  --rule:#d6d6d6;
  --white:#fff;
}
*{margin:0;padding:0;box-sizing:border-box}
html,body{width:1200px;height:3996px;overflow:hidden}
body{position:relative;background:var(--white);font-family:"Poppins",sans-serif;color:var(--ink)}
.abs{position:absolute}
.heading{font-family:"Jost",sans-serif;font-weight:600;font-size:29px;color:var(--blue);text-align:center;width:100%;left:0;letter-spacing:.2px}
.rule{position:absolute;left:552px;width:96px;height:3px;background:var(--blue)}
.btn{position:absolute;display:flex;align-items:center;justify-content:center;font-family:"Jost",sans-serif;font-size:19px;color:var(--white);background:var(--blue)}

/* header */
.header{position:absolute;left:0;top:0;width:1200px;height:143px;background:var(--white)}
.brand-panel{position:absolute;left:0;top:0}
.brand{position:absolute;left:120px;top:36px;width:170px;text-align:center;font-family:"Jost",sans-serif;font-weight:600;font-size:24px;line-height:28px;color:var(--white)}
.topnav{position:absolute;top:36px;left:0;width:1200px;font-family:"Poppins",sans-serif;font-size:14px;color:var(--ink)}
.topnav span{position:absolute;top:0;height:24px;line-height:24px;white-space:nowrap}
.topnav .active{background:#e4e4e4;padding:0 10px;left:563px}
.topline{position:absolute;left:505px;top:78px;width:583px;height:1px;background:var(--rule)}
.mainnav{position:absolute;top:98px;font-size:15px;color:var(--ink);height:24px;line-height:24px;white-space:nowrap}

/* hero */
.hero{position:absolute;left:0;top:143px;width:1200px;height:573px;background:linear-gradient(120deg,#6b4a36 0%,#8d6a52 30%,#3e3a3c 60%,#6e655f 100%)}
.hero-shade{position:absolute;inset:0;background:rgba(20,16,14,.35)}
.hero h1{position:absolute;top:275px;width:100%;text-align:center;font-family:"Jost",sans-serif;font-weight:500;font-size:44px;color:var(--white)}
.hero p{position:absolute;top:340px;left:220px;width:760px;text-align:center;font-family:"Jost",sans-serif;font-size:18px;line-height:29px;color:var(--white)}
.hero .outline{position:absolute;left:539px;top:429px;width:122px;height:49px;border:2px solid var(--white);display:flex;align-items:center;justify-content:center;font-family:"Jost",sans-serif;font-size:19px;color:var(--white)}

.rail{position:absolute;left:0;top:716px;width:1200px;height:94px;background:linear-gradient(#c8c8c8 0,#e2e2e2 36%,#f6f6f6 60%,#fff 100%)}

/* about */
.about p{position:absolute;left:112px;width:976px;text-align:center;font-size:13.5px;line-height:24px;color:var(--muted)}

/* blog */
.blog{position:absolute;left:112px;top:1215px;width:976px;height:455px;background:var(--navy)}
.blog .heading{color:var(--white);top:52px}
.card-img{position:absolute;top:166px;width:112px;height:170px}
.card-title{position:absolute;top:164px;font-family:"Jost",sans-serif;font-weight:500;font-size:19px;color:var(--white)}
.card-text{position:absolute;top:202px;width:150px;font-size:13px;line-height:22px;color:#dfe3f4}
.card-link{position:absolute;top:302px;font-size:13.5px;font-weight:500;color:var(--white)}
.dots{position:absolute;display:flex;gap:6px}
.dots i{display:block;width:14px;height:14px;border-radius:50%;background:#7f86a8}
.dots i.on{background:var(--white)}

/* products */
.product{position:absolute;width:300px;text-align:center}
.product .img{margin:0 auto;width:280px;height:160px}
.product h3{margin-top:16px;font-family:"Jost",sans-serif;font-weight:500;font-size:19px;color:var(--ink)}
.product p{margin:14px auto 0;width:250px;font-size:13.5px;line-height:24px;color:var(--muted)}

/* gallery */
.gallery{position:absolute;left:0;top:2660px;width:1200px;height:842px;background:var(--grey-bg)}
.gallery svg{position:absolute;left:0;top:166px}
.gallery .dots i{background:#6b7198}
.gallery .dots i.on{background:var(--navy)}

/* footer */
.footer{position:absolute;left:0;top:3502px;width:1200px;height:494px;background:radial-gradient(ellipse at 50% 20%,#1a2a7a 0%,var(--navy) 45%,var(--navy-deep) 100%)}
.footer .brand{left:515px;top:80px;width:170px;font-size:30px;line-height:34px}
.social{position:absolute;top:267px;left:505px;display:flex;gap:10px}
.social i{display:block;width:40px;height:40px;border:2px solid var(--white);border-radius:50%}
.footnav{position:absolute;top:344px;width:100%;text-align:center;font-size:15px;color:var(--white);word-spacing:2px}
.footnav b{font-weight:400;margin:0 12px}
.footline{position:absolute;left:112px;top:410px;width:976px;height:1px;background:#3a4480}
.copyright{position:absolute;top:442px;width:100%;text-align:center;font-size:14px;color:var(--white)}
</style>
</head>
<body>

<header class="header">
  <svg class="brand-panel" width="370" height="143" viewBox="0 0 370 143">
    <defs><linearGradient id="panelGrad" x1="0" y1="0" x2="1" y2="1"><stop offset="0" stop-color="#1c2f86"/><stop offset="1" stop-color="#081040"/></linearGradient></defs>
    <polygon points="0,0 365,0 305,143 0,143" fill="url(#panelGrad)"/>
  </svg>
  <div class="brand">ORRIN<br>LIGHTING</div>

  <nav class="topnav">
    <span class="active">HOME</span>
    <span style="left:640px">ABOUT</span>
    <span style="left:709px">NEWS</span>
    <span style="left:774px">CAREERS</span>
    <span style="left:861px">CONTACT</span>
    <span style="left:946px;top:-2px">
      <svg width="28" height="28" viewBox="0 0 28 28"><circle cx="14" cy="14" r="12.5" fill="none" stroke="#222" stroke-width="1.6"/><path d="M10 8.5c1-.6 1.7-.4 2.2.5l.9 1.8c.3.7.1 1.2-.5 1.6l-.7.5c.6 1.5 1.8 2.8 3.3 3.4l.5-.7c.4-.6 1-.8 1.6-.5l1.8.9c.9.5 1.1 1.2.5 2.2-1 1.6-2.8 1.8-4.7.8-2.6-1.3-4.6-3.4-5.8-6-.9-1.9-.6-3.6.9-4.5z" fill="#222"/></svg>
    </span>
    <span style="left:984px">+987 210 4365</span>
  </nav>
  <div class="topline"></div>
  <div class="mainnav" style="left:548px">PRODUCTS <svg width="14" height="10" viewBox="0 0 14 10"><path d="M1 2l6 6 6-6" fill="none" stroke="#555" stroke-width="2"/></svg></div>
  <div class="mainnav" style="left:688px">SOLUTIONS <svg width="14" height="10" viewBox="0 0 14 10"><path d="M1 2l6 6 6-6" fill="none" stroke="#555" stroke-width="2"/></svg></div>
  <div class="mainnav" style="left:825px">CASE STUDIES</div>
  <div class="mainnav" style="left:978px">DOWNLOADS</div>
</header>

<section class="hero" role="img" aria-label="Photo of people working at a long table in a brick-walled office under a hanging filament bulb">
  <div class="hero-shade"></div>
  <h1>WELCOME TO ORRIN LIGHTING</h1>
  <p>Nemo enim ipsam voluptatem quia voluptas sit aspernatur aut odit aut fugit sed consequuntur magni dolores.</p>
  <div class="outline">Read More</div>
</section>
<div class="rail" role="img" aria-label="Ceiling rail with a row of spotlights casting soft glows"></div>

<section class="about">
  <h2 class="heading abs" style="top:835px">ABOUT ORRIN LIGHTING</h2>
  <div class="rule" style="top:892px"></div>
  <p style="top:930px">Nemo enim ipsam voluptatem quia voluptas sit aspernatur aut odit aut fugit, sed quia consequuntur magni dolores eos qui ratione voluptatem sequi nesciunt. Neque porro quisquam est, qui dolorem ipsum quia dolor sit amet, consectetur, adipisci velit, sed quia non numquam eius modi tempora incidunt ut labore et dolore magnam aliquam quaerat voluptatem.</p>
  <p style="top:1016px">Dolorem ipsum quia dolor sit amet, consectetur, adipisci velit, sed quia non numquam eius modi tempora incidunt ut labore et dolore magnam aliquam quaerat voluptatem.</p>
  <div class="btn" style="left:539px;top:1101px;width:122px;height:50px">Read More</div>
</section>

<section class="blog">
  <h2 class="heading abs">LATEST BLOG POSTS</h2>
  <div class="rule" style="left:440px;top:106px;background:#fff"></div>

  <div class="card-img" role="img" aria-label="Open-plan office interior" style="left:30px;background:linear-gradient(135deg,#b9c0c6,#6f7a82)"></div>
  <div class="card-title" style="left:154px">Nemo Enim Ipsam</div>
  <div class="card-text" style="left:156px">Nemo enim ipsam voluptatem quia voluptas sit aut odit fonsequuntur.</div>
  <div class="card-link" style="left:156px">Read More &gt;&gt;</div>

  <div class="card-img" role="img" aria-label="Office with desks under ceiling panel lights" style="left:355px;background:linear-gradient(135deg,#e4e7ea,#8c959e)"></div>
  <div class="card-title" style="left:479px">Nemo Enim Ipsam</div>
  <div class="card-text" style="left:481px">Nemo enim ipsam voluptatem quia voluptas sit aut odit fonsequuntur.</div>
  <div class="card-link" style="left:481px">Read More &gt;&gt;</div>

  <div class="card-img" role="img" aria-label="Bright office corridor with glass walls" style="left:672px;background:linear-gradient(135deg,#eef0f1,#a4abb1)"></div>
  <div class="card-title" style="left:796px">Nemo Enim Ipsam</div>
  <div class="card-text" style="left:798px">Nemo enim ipsam voluptatem quia voluptas sit aut odit fonsequuntur.</div>
  <div class="card-link" style="left:798px">Read More &gt;&gt;</div>

  <div class="dots" style="left:440px;top:393px"><i class="on"></i><i></i><i></i><i></i><i></i></div>
</section>

<section class="products">
  <h2 class="heading abs" style="top:1750px">OUR PRODUCTS</h2>
  <div class="rule" style="top:1808px"></div>

  <div class="product" style="left:107px;top:1870px"><div class="img" role="img" aria-label="Linear LED batten lights" style="background:linear-gradient(#fff,#eceef0 50%,#fff)"></div><h3>Ullam Corporis Suscipit</h3><p>Nemo enim ipsam voluptatem quia voluptas.</p></div>
  <div class="product" style="left:458px;top:1870px"><div class="img" role="img" aria-label="Round LED downlight" style="background:radial-gradient(circle,#e8eaec 0,#f7f7f7 45%,#fff 60%)"></div><h3>Ullam Corporis Suscipit</h3><p>Nemo enim ipsam voluptatem quia voluptas.</p></div>
  <div class="product" style="left:805px;top:1870px"><div class="img" role="img" aria-label="Cylindrical pendant light" style="background:radial-gradient(ellipse at 50% 45%,#e6e6e6 0,#f8f8f8 30%,#fff 55%)"></div><h3>Ullam Corporis Suscipit</h3><p>Nemo enim ipsam voluptatem quia voluptas.</p></div>

  <div class="product" style="left:107px;top:2178px"><div class="img" role="img" aria-label="Suspended linear pendant light" style="background:linear-gradient(#fff,#f1f1f1 80%,#fff)"></div><h3>Ullam Corporis Suscipit</h3><p>Nemo enim ipsam voluptatem quia voluptas.</p></div>
  <div class="product" style="left:458px;top:2178px"><div class="img" role="img" aria-label="Slim round panel light" style="background:radial-gradient(circle,#fdfbe8 0,#eef0f3 40%,#fff 58%)"></div><h3>Ullam Corporis Suscipit</h3><p>Nemo enim ipsam voluptatem quia voluptas.</p></div>
  <div class="product" style="left:805px;top:2178px"><div class="img" role="img" aria-label="Industrial high bay light" style="background:radial-gradient(ellipse at 50% 60%,#c9b79a 0,#e9e3d8 35%,#fff 60%)"></div><h3>Ullam Corporis Suscipit</h3><p>Nemo enim ipsam voluptatem quia voluptas.</p></div>

  <div class="btn" style="left:512px;top:2490px;width:176px;height:50px">View All Products</div>
</section>

<section class="gallery">
  <h2 class="heading abs" style="top:58px">OUR GALLERY</h2>
  <div class="rule" style="top:116px"></div>
  <svg width="1200" height="545" viewBox="0 0 1200 545">
    <g>
      <polygon points="60,0 425,0 378,259 20,259" fill="#b8c4c8" role="img" aria-label="Open-plan office with yellow chairs"/>
      <polygon points="438,0 803,0 756,259 398,259" fill="#bfa48c" role="img" aria-label="Desk in front of a brick wall with track lights"/>
      <polygon points="816,0 1180,0 1133,259 776,259" fill="#9a9a96" role="img" aria-label="Lobby with lounge seating"/>
      <polygon points="60,282 425,282 378,542 20,542" fill="#c3ccd0" role="img" aria-label="Bright office with columns and yellow chairs"/>
      <polygon points="438,282 803,282 756,542 398,542" fill="#5e4a3c" role="img" aria-label="Industrial workspace with wooden desks"/>
      <polygon points="816,282 1180,282 1133,542 776,542" fill="#6c5240" role="img" aria-label="Corridor with glass meeting rooms"/>
    </g>
  </svg>
  <div class="dots" style="left:552px;top:765px"><i class="on"></i><i></i><i></i><i></i><i></i></div>
</section>

<footer class="footer">
  <div class="brand">ORRIN<br>LIGHTING</div>
  <div class="social" aria-label="Social links"><i></i><i></i><i></i><i></i></div>
  <div class="footnav">HOME<b>|</b>ABOUT US<b>|</b>NEWS<b>|</b>CAREERS<b>|</b>CASE STUDIES<b>|</b>CONTACT US</div>
  <div class="footline"></div>
  <div class="copyright">Copyrights @ 2019 Orrin Lighting. All Rights Reserved.</div>
</footer>

</body>
</html>
```